Portfolio site - Need a basic WordPress or SquareSpace site

I need a portfolio site where I have the option to keep updating it on my own. Therefore, I'm guessing I need one that uses WordPress or SquareSpace. I just need a simple and elegant design. I'm a writer (scholarly, fiction and journalism).

Target Market(s)

Adult

Industry/Entity Type

Writer

Number of Pages Required

4 page

Font styles to use
Serif

Colors
b7a5cd
e667a6
85abd2

Requirements
Must have
• Easily updatable features. I'll have to publish links and small blurbs from time to time. And maybe the occasional image.
• Pages should be:
• Home
• Work
• Press
• Contact

```html
<!DOCTYPE html>
<html lang="en">
<head>
<meta charset="utf-8">
<title>Mariam Elwood — Writer</title>
<link rel="stylesheet" href="https://fonts.googleapis.com/css2?family=Bodoni+Moda:wght@700&family=Cormorant+Garamond:wght@400;500&family=Libre+Baskerville:wght@400&display=swap">
<style>
  :root {
    --pink: #e667a6;
    --lilac: #b7a5cd;
    --sky: #85abd2;
    --ink: #1a1a1a;
    --ink-soft: #333;
    --nav-active: #2f3cf0;
    --rule-green: #4bd24b;
    --card-bg: #ffffff;
    --rule-grey: #c4c4c4;
    --tile: #d9d2e4;
    --photo-warm: #8a7a6a;
    --photo-green: #2f5a3e;
    --photo-dark: #2a2a2a;
  }
  * { box-sizing: border-box; margin: 0; padding: 0; }
  html, body { width: 1136px; height: 1200px; overflow: hidden; background: #fff; }
  body { position: relative; font-family: "Cormorant Garamond", Georgia, serif; color: var(--ink); }

  .site-header {
    position: absolute; left: 0; top: 0; width: 1136px; height: 93px;
    background: var(--pink); box-shadow: 0 3px 4px rgba(0,0,0,.3); z-index: 2;
  }
  .brand {
    position: absolute; left: 200px; top: 38px;
    font-family: "Libre Baskerville", Georgia, serif; font-size: 15px; color: var(--ink);
  }
  .main-nav { position: absolute; top: 51px; left: 0; font-family: "Libre Baskerville", Georgia, serif; font-size: 12.5px; }
  .main-nav a { position: absolute; color: var(--ink-soft); text-decoration: none; white-space: nowrap; }
  .main-nav a.is-active { color: var(--nav-active); }

  .hero {
    position: absolute; left: 0; top: 0; width: 1136px; height: 487px;
    background: var(--pink); border-bottom: 1.5px solid var(--rule-green);
  }
  .hero-title {
    position: absolute; left: 0; width: 1165px; top: 231px; text-align: center;
    font-family: "Cormorant Garamond", Georgia, serif; font-weight: 500; font-size: 22px; letter-spacing: .3px;
  }
  .hero-text {
    position: absolute; left: 244px; top: 297px; width: 676px;
    font-size: 12.4px; line-height: 19.2px; color: #2a1a22;
  }

  .team-title {
    position: absolute; left: 0; width: 1080px; top: 500px; text-align: center;
    font-family: "Bodoni Moda", Georgia, serif; font-weight: 700; font-size: 50px; letter-spacing: 1px;
  }
  .team-card {
    position: absolute; top: 641px; width: 240px; height: 400px;
    background: var(--card-bg); border-radius: 6px; box-shadow: 0 2px 6px rgba(0,0,0,.35);
  }
  .team-photo { position: absolute; width: 115px; height: 115px; border-radius: 50%; }
  .team-bio { position: absolute; font-size: 10.6px; line-height: 19.2px; color: var(--ink-soft); }

  .footer-rule {
    position: absolute; left: 176px; top: 1054px; width: 768px; height: 9px;
    border: 1.5px solid var(--rule-grey);
  }
  .footer-brand {
    position: absolute; left: 162px; top: 1117px;
    font-family: "Libre Baskerville", Georgia, serif; font-size: 13px; color: var(--ink);
  }
  .social-link {
    position: absolute; top: 1064px; width: 72px; height: 72px; border-radius: 6px;
    background: var(--tile); display: flex; align-items: center; justify-content: center;
    font-family: "Cormorant Garamond", Georgia, serif; font-size: 12px; color: var(--ink-soft); text-decoration: none;
  }
  .copyright {
    position: absolute; left: 0; width: 1138px; top: 1171px; text-align: center;
    font-family: "Libre Baskerville", Georgia, serif; font-size: 9.5px; letter-spacing: 2.6px; color: var(--sky);
  }
</style>
</head>
<body>
  <section class="hero">
    <h1 class="hero-title">WE SPECIALISE ON SCHOLARLY, JOURNALS AND FICTION</h1>
    <p class="hero-text">Lorem ipsum dolor sit amet, consectetur adipisicing elit, sed do eiusmod tempor incididunt ut labore et dolore magna aliqua. Ut enim ad minim veniam, quis nostrud exercitation ullamco laboris nisi ut aliquip ex ea commodo consequat. Duis aute irure dolor in reprehenderit in voluptate velit esse cillum dolore eu fugiat nulla pariatur. Excepteur sint occaecat cupidatat non proident, sunt in culpa qui officia deserunt mollit anim id est laborum. Sed ut perspiciatis unde omnis iste natus error sit voluptatem accusantium doloremque laudantium, totam rem aperiam, eaque ipsa quae ab illo inventore veritatis et quasi architecto beatae vitae dicta sunt explicabo. Nemo enim ipsam voluptatem quia voluptas sit aspernatur aut odit aut fugit, sed quia consequuntur magni dolores eos qui ratione voluptatem sequi nesciunt. Neque porro quisquam est, qui dolorem ipsum quia dolor sit amet, consectetur, adipisci velit, sed quia non numquam eius modi tempora incidunt ut labore et dolore magnam aliquam quaerat voluptatem.</p>
  </section>

  <header class="site-header">
    <div class="brand">Mariam Elwood</div>
    <nav class="main-nav">
      <a class="is-active" href="#" style="left:559px">HOME</a>
      <a href="#" style="left:654px">WORK</a>
      <a href="#" style="left:756px">PRESS</a>
      <a href="#" style="left:870px">CONTACT</a>
    </nav>
  </header>

  <h2 class="team-title">MY TEAM</h2>

  <article class="team-card" style="left:150px">
    <div class="team-photo" role="img" aria-label="Portrait photo of a team member" style="left:63px;top:9px;background:radial-gradient(circle at 50% 45%, #a08a78, var(--photo-warm) 60%, #5a4a3e)"></div>
    <p class="team-bio" style="left:4px;top:197px;width:232px">Lorem ipsum dolor sit amet, consectetur adipisicing elit, sed do eiusmod tempor incididunt ut labore et dolore magna aliqua. Ut oluptate velit esse cillum dolore easpersquam est, qui dolorem ipsum quia dolor sit amet, consectetur, ed do eiusmod tempor incididunt ut labore et dolore magna aliqua. Ut oluptate velit esse qui dolorem ipsum quia dolor sit amet, consectetur,</p>
  </article>

  <article class="team-card" style="left:414px">
    <div class="team-photo" role="img" aria-label="Portrait photo of a team member" style="left:52px;top:21px;background:radial-gradient(circle at 55% 50%, #c9b9a4, var(--photo-green) 55%, #1e3a28)"></div>
    <p class="team-bio" style="left:8px;top:183px;width:232px">Lorem ipsum dolor sit aLorem ipsum dolor sit amet, coexplicabo. Nemo enim ipsam voluptatem quia voluptas sit asi velit, sed quia non numquam eius modi tempora incidunt ut labore et dolore magnam aliquam quaerat voluptatem.cabo. Nemo enim ipsam voluptatem quia voluptas sit asi velit, sed quia non numquam eius modi tempora incidunt ut labore et dolore magnam</p>
  </article>

  <article class="team-card" style="left:677px">
    <div class="team-photo" role="img" aria-label="Black and white portrait photo of a team member" style="left:50px;top:9px;background:radial-gradient(circle at 45% 45%, #6a6a6a, var(--photo-dark) 55%, #0e0e0e)"></div>
    <p class="team-bio" style="left:3px;top:185px;width:236px">&nbsp;Lorem ipsum dolor sit amet, pariatur. Exceaccusantium doloremque laudvoluptatem quia voluptas sit aspeia non numquam eius modi tempora incidunt ut labore et dolore magnam aliquam quaerat voluptatem.it aspeia non numquam eius modi tempora incidunt ut labore et dolore magnam aliquam quaerat voluptatem.</p>
  </article>

  <div class="footer-rule"></div>
  <div class="footer-brand">Mariam Elwood</div>

  <a class="social-link" href="#" style="left:381px">Friendline</a>
  <a class="social-link" href="#" style="left:472px">Snapframe</a>
  <a class="social-link" href="#" style="left:563px">Workring</a>
  <a class="social-link" href="#" style="left:654px">Circlenet</a>
  <a class="social-link" href="#" style="left:746px">Clipcast</a>
  <a class="social-link" href="#" style="left:837px">Chirpline</a>

  <p class="copyright">copyright 2018 Mariam Elwood. All right Reserved</p>
</body>
</html>
```